Email signatures and letterhead for in-house lawyers and staff

I need Word, Outlook, and Gmail compatible letterhead and email signature block for an in-house litigation group. Simple and generic is the goal! The design must be user-modifiable for several locations and job titles. The design will work best if created in MS Word. We are an in-house group of trial lawyers, about 40 persons total, operating from nine locations, and providing services in ten US states. Letterhead will be used in header of MSWord documents. Email sig will be used in both Outlook and Gmail. The office name will be different in each of our locations, so the design has to be user-modifiable.

Industry/Entity Type

Law Firm

Font styles to use
Sans Serif

Requirements
Must have
• A fresher, more professional look than the screenshots I've posted

The screenshot with multiple attorney names in the office is most representative of the info we want included.
Nice to have
• Sylish but not overly so. Generic legal symbols might be appropriate, but can't look like tired old clip art.
Should not have
• watermarks

```html
<!DOCTYPE html>
<html lang="en">
<head>
<meta charset="utf-8">
<title>Letterhead – Law Office of Daniel Hartwell</title>
<link rel="stylesheet" href="https://fonts.googleapis.com/css2?family=Libre+Baskerville&family=Montserrat:wght@600;700&family=Questrial&display=swap">
<style>
  :root {
    --gold: #b8873f;
    --ink: #000000;
    --paper: #ffffff;
    --desk: #d4d4d4;
    --text: #3a3a3a;
    --muted: #6b6b6b;
  }
  * { margin: 0; padding: 0; box-sizing: border-box; }
  html, body { width: 1200px; height: 1200px; overflow: hidden; }
  body { background: var(--desk); position: relative; font-family: "Questrial", "Century Gothic", sans-serif; }

  .letterhead {
    position: absolute; left: 160px; top: 30px;
    width: 880px; height: 1140px;
    background: var(--paper);
    overflow: hidden;
    box-shadow: 0 6px 24px rgba(0,0,0,.18);
  }
  .bands { position: absolute; left: 0; width: 880px; }
  .bands--top { top: 0; height: 120px; }
  .bands--bottom { bottom: 0; height: 180px; }

  .partners {
    position: absolute; left: 470px; top: 16px; width: 380px;
    font-family: "Libre Baskerville", "Times New Roman", serif;
    color: var(--paper); font-size: 17px; line-height: 1.45;
  }

  .firm { position: absolute; left: 48px; top: 62px; display: flex; align-items: center; gap: 16px; }
  .firm__dot { width: 44px; height: 44px; border-radius: 50%; border: 1.5px solid var(--gold); }
  .firm__name {
    font-family: "Libre Baskerville", "Times New Roman", serif;
    color: var(--gold); font-size: 24px; line-height: 1.2;
  }
  .firm__name small { display: block; font-size: 15px; }

  .sender { position: absolute; left: 110px; top: 170px; color: var(--muted); font-size: 13px; line-height: 1.6; }

  .recipient { position: absolute; left: 110px; top: 300px; }
  .recipient__name { font-family: "Montserrat", sans-serif; font-weight: 700; font-size: 16px; color: var(--muted); }
  .recipient__address { font-size: 14px; color: var(--ink); margin-top: 4px; }

  .letter { position: absolute; left: 110px; top: 390px; width: 700px; font-size: 13.5px; line-height: 1.6; color: var(--muted); }
  .letter__greeting { color: var(--ink); font-size: 14.5px; margin-bottom: 14px; }
  .letter p { margin-bottom: 12px; }
  .letter__closing { margin-top: 30px; }

  .signature { position: absolute; left: 110px; top: 820px; }
  .signature__name { font-family: "Montserrat", sans-serif; font-weight: 600; font-size: 14px; color: var(--ink); }
  .signature__title { font-size: 13px; color: var(--ink); margin-top: 10px; }

  .contact {
    position: absolute; left: 40px; bottom: 22px;
    font-family: "Libre Baskerville", "Times New Roman", serif;
    color: var(--paper); font-size: 15px; line-height: 1.6;
  }
  .contact b { font-weight: 400; }
</style>
</head>
<body>
  <main class="letterhead">
    <svg class="bands bands--top" viewBox="0 0 880 120" aria-hidden="true">
      <polygon points="0,0 380,0 430,30 0,30" fill="var(--gold)"/>
      <polygon points="330,0 880,0 880,55 430,112" fill="var(--ink)"/>
    </svg>
    <div class="partners">Daniel Hartwell, Miriam Oakes,<br>Tobias Renner</div>

    <div class="firm">
      <span class="firm__dot"></span>
      <div class="firm__name"><small>Law Office of</small>Daniel Hartwell</div>
    </div>

    <div class="sender">[Company Name]<br>[Street Address, City, ST ZIP Code]<br>[Phone]<br>[Email]<br>[Website]</div>

    <div class="recipient">
      <div class="recipient__name">Recipient Name</div>
      <div class="recipient__address">Street Address, City, ST ZIP Code</div>
    </div>

    <article class="letter">
      <p class="letter__greeting">Dear Recipient,</p>
      <p>Lorem ipsum dolor sit amet, consectetuer adipiscing elit. Maecenas porttitor congue massa. Fusce posuere, magna sed pulvinar ultricies, purus lectus malesuada libero, sit amet commodo magna eros quis urna.</p>
      <p>Nunc viverra imperdiet enim. Fusce est. Vivamus a tellus.</p>
      <p>Pellentesque habitant morbi tristique senectus et netus et malesuada fames ac turpis egestas. Proin pharetra nonummy pede. Mauris et orci.</p>
      <p>Aenean nec lorem. In porttitor. Donec laoreet nonummy augue.</p>
      <p>Suspendisse dui purus, scelerisque at, vulputate vitae, pretium mattis, nunc. Mauris eget neque at sem venenatis eleifend. Ut nonummy.</p>
      <p class="letter__closing">Warm regards,</p>
    </article>

    <div class="signature">
      <div class="signature__name">Name Here</div>
      <div class="signature__title">Your Title</div>
    </div>

    <svg class="bands bands--bottom" viewBox="0 0 880 180" aria-hidden="true">
      <polygon points="690,20 880,0 880,28 770,60" fill="var(--ink)"/>
      <polygon points="0,78 520,78 610,40 840,40 880,28 880,180 0,180" fill="var(--gold)"/>
    </svg>
    <div class="contact">
      482 Linden Ridge Avenue, Suite 310, Brookvale XY 40218<br>
      <b>P:</b> (555) 240-1187 <b>F:</b> (555) 240-1190 <b>E:</b> office@hartwell-law.example
    </div>
  </main>
</body>
</html>
```